Project Manager Business Card for Top Architectural Firm

Update and design a stunning Senior Project Manager Business Card

MARCO T. DRUMMOND II
Senior Project Manager

H A L C Y O N
A R C H I T E C T U R E L L C.
www.HalcyonGrandEstates.example
4127 NW 52nd Ter. Suite 2308
Miami, FL 33148
C: (305) 555-0184
mdrummond.halcyongrandestates@mailbox.example

Looking to have the logo to be UV Spot ink printed and to be prominent.

Target Market(s)

High end real estate architecture construction

Industry/Entity Type

Architect

Contact Information for Business Card

MARCO T. DRUMMOND II
Senior Project Manager

H A L C Y O N
Miami, FL 33148
C: (305) 555-0184

Font styles to use
Sans Serif

Colors

Designer to choose colors to be used in the design.

Requirements
Must have
• Prominent Logo

```html
<!DOCTYPE html>
<html lang="en">
<head>
<meta charset="utf-8">
<title>Halcyon Architecture – Business Card</title>
<link rel="stylesheet" href="https://fonts.googleapis.com/css2?family=Oswald:wght@300&family=Roboto:wght@400&display=swap">
<style>
  :root {
    --backdrop: #3a3a3c;
    --card: #1f1f21;
    --card-edge: #2a2a2c;
    --white: #f2f2f2;
    --soft: #8a8a8e;
    --blue: #1f8fd6;
    --sky: #5bb4ea;
    --orange: #ef8a2e;
    --red: #b8424a;
    --navy: #2f4a6e;
  }
  * { margin: 0; padding: 0; box-sizing: border-box; }
  html, body { width: 799px; height: 1200px; overflow: hidden; }
  body {
    background: var(--backdrop);
    font-family: "Roboto", Arial, sans-serif;
    color: var(--white);
    position: relative;
  }
  .card {
    position: absolute;
    left: 90px;
    width: 620px;
    height: 354px;
    background: var(--card);
    border: 1px solid var(--card-edge);
    border-radius: 4px;
    box-shadow: 0 18px 40px rgba(0,0,0,.45);
    overflow: hidden;
  }
  .card--front { top: 130px; }
  .card--back { top: 730px; }

  .front-mark {
    position: absolute;
    inset: 0;
    display: flex;
    align-items: center;
    justify-content: center;
    gap: 18px;
  }
  .front-mark__dot {
    width: 26px; height: 26px; border-radius: 50%;
    background: var(--soft);
  }
  .front-mark__name {
    font-family: "Oswald", Arial, sans-serif;
    font-weight: 300;
    font-size: 46px;
    letter-spacing: 14px;
    color: var(--soft);
  }

  .person { position: absolute; left: 34px; top: 30px; }
  .person__name {
    font-family: "Oswald", Arial, sans-serif;
    font-weight: 300;
    font-size: 30px;
    color: var(--blue);
    line-height: 1.05;
  }
  .person__role { font-size: 14px; margin-top: 4px; }

  .contact { position: absolute; left: 34px; top: 150px; font-size: 13px; line-height: 1.5; }
  .contact__address { margin-bottom: 12px; }
  .contact__row { display: flex; align-items: center; gap: 10px; }
  .contact__row svg { width: 12px; height: 12px; flex: none; }
  .contact__web { padding-left: 22px; }

  .wordmark {
    position: absolute; right: 34px; top: 120px;
    font-family: "Oswald", Arial, sans-serif;
    font-weight: 300;
    color: var(--white);
    text-align: right;
  }
  .wordmark__name { font-size: 40px; letter-spacing: 9px; line-height: 1; }
  .wordmark__sub { font-size: 10px; letter-spacing: 3px; margin-top: 4px; }

  .stripe { position: absolute; left: 0; right: 0; bottom: 0; height: 6px; display: flex; }
  .stripe span { flex: 1; }
  .s-orange { background: var(--orange); }
  .s-red { background: var(--red); }
  .s-navy { background: var(--navy); }
  .s-blue { background: var(--blue); }
  .s-sky { background: var(--sky); }
</style>
</head>
<body>
  <section class="card card--front" aria-label="Card front">
    <div class="front-mark">
      <span class="front-mark__dot"></span>
      <span class="front-mark__name">HALCYON</span>
    </div>
  </section>

  <section class="card card--back" aria-label="Card back">
    <div class="person">
      <h1 class="person__name">MARCO T. DRUMMOND II</h1>
      <p class="person__role">Senior Project Manager</p>
    </div>

    <div class="contact">
      <p class="contact__address">4127 NW 52nd Ter. Suite 2308<br>Miami, FL 33148</p>
      <p class="contact__row">
        <svg viewBox="0 0 12 12"><path fill="var(--orange)" d="M2 1h2.5l1 3-1.5 1a6 6 0 0 0 3 3l1-1.5 3 1V11C6 11 1 6 1 2z"/></svg>
        (305) 555-0184
      </p>
      <p class="contact__row">
        <svg viewBox="0 0 12 12"><rect x="1" y="2.5" width="10" height="7" fill="var(--orange)"/><path d="M1 2.5l5 4 5-4" stroke="var(--card)" fill="none"/></svg>
        mdrummond.halcyongrandestates@mailbox.example
      </p>
      <p class="contact__row">
        <svg viewBox="0 0 12 12"><circle cx="6" cy="6" r="5" fill="var(--orange)"/><path d="M1 6h10M6 1v10M6 1c-2.5 3-2.5 7 0 10M6 1c2.5 3 2.5 7 0 10" stroke="var(--card)" stroke-width=".7" fill="none"/></svg>
        www.HalcyonGrandEstates.example
      </p>
    </div>

    <div class="wordmark">
      <p class="wordmark__name">HALCYON</p>
      <p class="wordmark__sub">ARCHITECTURE LLC.</p>
    </div>

    <div class="stripe">
      <span class="s-orange"></span><span class="s-red"></span><span class="s-navy"></span><span class="s-blue"></span><span class="s-sky"></span>
      <span class="s-orange"></span><span class="s-red"></span><span class="s-navy"></span><span class="s-blue"></span><span class="s-sky"></span>
    </div>
  </section>
</body>
</html>
```